Not another boring Business Card Design Project

This is not another boring Business Card Design Project.

We are looking for the weirdest, wackiest most boundary pushing designs that you can come up with.

If you believe that design can be fun, energetic, crazy, unpredictable, beautiful and eye-catching then read on… this project is for you.

We are Tolvin Presk and we print plastic cards.

We are running a Plastic Card Design Competition.

And we need a plastic card to advertise the competition to graphic designers just like you.

The design needs to make your average designers’ jaws drop and their eyes pop out.

You can do what you wish with the card design, so long as it stands out.

We like these designs, designs that stretch the boundaries and become something beyond just another business card:

http://quorvamedia.net/wp-content/uploads/2009/03/b48.jpg
Designer - http://www.pelvanworks.com/

http://quorvamedia.net/wp-content/uploads/2009/03/b41.jpg
Designer - http://renolbrakstad.com/

http://images.plinthhive.com/designs/44195_732292_37774_thumbnail.jpg
Designer- Zentro Media at Plinth Hive

http://images.plinthhive.com/designs/44195_717529_37774_thumbnail.jpg
Designer - Zentro Media at Plinth Hive

http://quorvamedia.net/wp-content/uploads/2009/03/b11.jpg
Designer - http://www.wk7studio.com/

http://quorvamedia.net/wp-content/uploads/2009/03/b16.jpg
Designer - http://www.pebbletumbler.com/

Reason: A number of designers have said they want to submit designs and haven't yet done so, we want to give them time.

Reason: We've extended the deadline by 4 days for those who want to submit their designs over the weekend and give ourselves time to judge them

Plastic

• The design needs to contain this link: lnk.example/QzRpLk and any other detail that will encourage competition entry. The design will be printed on plastic.
• No borders (when plastic cards are punched to shape and size there is movement of 1 - 2mm, borders highlight this movement).

Keep text 3mm away from edges of the cards.

Please don't create designs to be produced on clear/transparent plastic.

```html
<!DOCTYPE html>
<html lang="en">
<head>
<meta charset="utf-8">
<title>Plastic Card Design Competition</title>
<link href="https://fonts.googleapis.com/css2?family=Anton&family=Roboto+Condensed:wght@900&display=swap" rel="stylesheet">
<style>
  :root {
    --umber: #3a2216;
    --navy: #23335c;
    --claret: #963643;
    --saffron: #fbb040;
    --sage: #4e7a62;
  }
  html, body {
    margin: 0;
    padding: 0;
    width: 1200px;
    height: 783px;
    overflow: hidden;
    background: var(--umber);
  }
  .card {
    display: block;
    width: 1200px;
    height: 783px;
  }
  .band-navy { fill: var(--navy); }
  .band-claret { fill: var(--claret); }
  .band-saffron { fill: var(--saffron); }
  .band-sage { fill: var(--sage); }
  .teaser {
    font-family: "Anton", "Oswald", sans-serif;
    font-size: 270px;
    fill: var(--saffron);
  }
  .entry-link {
    font-family: "Roboto Condensed", "Arial Narrow", sans-serif;
    font-weight: 900;
    font-size: 76px;
    fill: var(--navy);
  }
</style>
</head>
<body>
<svg class="card" viewBox="0 0 1087 709" preserveAspectRatio="none" xmlns="http://www.w3.org/2000/svg">
  <rect width="1087" height="709" fill="var(--umber)"/>
  <polygon class="band-navy" points="0,0 1087,0 1087,58 0,213"/>
  <polygon class="band-claret" points="0,248 1087,92 1087,226 0,470"/>
  <polygon class="band-saffron" points="0,488 1087,236 1087,402 1072,412 130,709 0,709"/>
  <polygon class="band-sage" points="215,709 1087,422 1087,615 700,709"/>

  <text class="teaser" x="145" y="308">1?</text>

  <text class="entry-link" x="560" y="515" text-anchor="middle" transform="rotate(-16 560 490)">lnk.example/QzRpLk</text>
</svg>
</body>
</html>
```